Brochure to attract insurance agents to outsource their bookkeeping

I need a brochure to handout at trade shows. Company name is Marrowfield Tally & Ledger Services. We go by MTLS. We provide bookkeeping services. I have attached the current brochure, which is a few years old, stale and outdated (not created on ArtQuorra). I have also attached our graphic identity manual which show fonts/colors as well as our logo in 3 styles

Target Market(s)

Insurance Agents needing bookkeeping services

Industry/Entity Type

Accounting

Other font styles liked:
• See the graphic id manual

Colors
00AB8E
00BBA5
67D7C9
C6EFE9
E9F9F6

Requirements
Must have
• Services noted (see current brochure), contact info, reference to Velmont Orbis

```html
<!DOCTYPE html>
<html lang="en">
<head>
<meta charset="utf-8">
<title>MTLS Trifold Brochure</title>
<link href="https://fonts.googleapis.com/css2?family=Montserrat:wght@300;400;500;600;700;800&family=Oswald:wght@500;600&display=swap" rel="stylesheet">
<style>
:root{
  --teal:#00ab8e;
  --teal-mid:#00bba5;
  --teal-deep:#0b8576;
  --teal-light:#67d7c9;
  --mint:#c6efe9;
  --mist:#e9f9f6;
  --ink:#2b2b2b;
  --grey:#6f6f6f;
  --grey-light:#d9d9d9;
  --page:#ebebeb;
  --white:#ffffff;
}
*{box-sizing:border-box;margin:0;padding:0}
html,body{width:808px;height:1200px;overflow:hidden}
body{background:var(--page);font-family:'Montserrat',sans-serif;color:var(--ink);position:relative}
.sheet{position:absolute;left:69px;width:670px;height:521px;overflow:hidden;background:var(--white);box-shadow:0 2px 6px rgba(0,0,0,.18)}
.sheet--outside{top:66px}
.sheet--inside{top:613px}
.sheet-bg{position:absolute;left:0;top:0}
.abs{position:absolute}
.tab{position:absolute;font-family:'Oswald',sans-serif;font-weight:500;text-transform:uppercase;display:flex;align-items:center;white-space:nowrap;width:auto;padding-right:12px;letter-spacing:0}
.tab--teal{background:var(--teal);color:var(--white);border-radius:0 16px 16px 0;box-shadow:2px 2px 4px rgba(0,0,0,.2)}
.tab--white{background:var(--white);color:var(--teal);border-radius:0 16px 16px 0;box-shadow:2px 2px 5px rgba(0,0,0,.25)}
.svc{position:absolute;width:57px;height:57px}
.svc-label{position:absolute;width:84px;text-align:center;font-size:6.2px;font-weight:700;line-height:7.7px;text-transform:uppercase;color:var(--ink)}
.body-text{position:absolute;font-size:7px;line-height:8.9px;text-align:justify}
.steps{position:absolute;left:248px;top:0}
.step{position:absolute;left:9px;width:168px;font-size:7px;line-height:8.9px;color:var(--white);text-align:justify}
.step-tick{position:absolute;left:-13px;top:0}
.step-line{position:absolute;left:-8.5px;width:1px;background:rgba(255,255,255,.7)}
.web{position:absolute;top:490px;width:223px;text-align:center;font-size:7.2px;font-weight:700;letter-spacing:.1px}
.feature-label{position:absolute;font-size:5.6px;font-weight:700;white-space:nowrap}
.headline{position:absolute;right:16px;top:365px;text-align:right;font-size:18.5px;line-height:17px;font-weight:300;color:var(--ink)}
.headline .alt{color:var(--grey)}
.headline strong{color:var(--teal);font-weight:700}
.brand{position:absolute;left:454px;top:30px;color:var(--teal);font-weight:700;display:flex;align-items:center;gap:5px}
.brand-mark{width:9px;height:9px;background:var(--teal)}
.brand-name{font-size:24px;line-height:24px;letter-spacing:1px}
.brand-full{position:absolute;left:454px;top:56px;width:130px;font-size:6px;line-height:7px;color:var(--teal);font-weight:700}
.person-name{position:absolute;width:222px;text-align:center;font-size:8.8px;font-weight:500}
.person-role{position:absolute;width:222px;text-align:center;font-size:7.6px;font-weight:600}
.contact-line{position:absolute;left:222px;width:225px;text-align:center}
.fee-table{position:absolute;left:478px;top:242px;width:156px;height:99px;border:1px solid rgba(255,255,255,.8);border-top:none;border-radius:0 0 8px 8px}
.fee-head{display:flex;height:25px;background:linear-gradient(180deg,#f4f4f4,#cfcfcf);color:#555;font-size:6.8px;font-weight:500;line-height:8px}
.fee-head div{width:50%;padding:4px 4px 0 5px}
.fee-head div+div{border-left:1px solid #bbb}
.fee-body{display:flex;color:var(--white);font-size:7.6px;line-height:9px;font-weight:500;height:73px}
.fee-body div{width:50%;padding:5px 0 0 5px}
.fee-body div+div{border-left:1px solid rgba(255,255,255,.8)}
</style>
</head>
<body>

<svg width="0" height="0" style="position:absolute" aria-hidden="true">
  <defs>
    <linearGradient id="g-teal-panel" x1="0" y1="0" x2="1" y2="1">
      <stop offset="0" stop-color="#0d8f80"/><stop offset=".5" stop-color="#14a393"/><stop offset="1" stop-color="#0a7f71"/>
    </linearGradient>
    <linearGradient id="g-grey" x1="0" y1="0" x2="1" y2="0">
      <stop offset="0" stop-color="#c9c9c9"/><stop offset="1" stop-color="#f2f2f2"/>
    </linearGradient>
    <linearGradient id="g-grey-v" x1="0" y1="0" x2="0" y2="1">
      <stop offset="0" stop-color="#e4e4e4"/><stop offset="1" stop-color="#bdbdbd"/>
    </linearGradient>
    <radialGradient id="g-circle" cx=".4" cy=".35" r=".7">
      <stop offset="0" stop-color="#1fc2aa"/><stop offset="1" stop-color="#00957c"/>
    </radialGradient>
    <symbol id="svc-ring" viewBox="0 0 57 57">
      <circle cx="28.5" cy="28.5" r="27.5" fill="#fff" stroke="#c8c8c8" stroke-width="1"/>
      <circle cx="28.5" cy="28.5" r="24.5" fill="url(#g-circle)"/>
    </symbol>
    <symbol id="tick" viewBox="0 0 10 10">
      <circle cx="5" cy="5" r="4.6" fill="#fff"/>
      <path d="M2.8 5.1l1.5 1.5 3-3.1" fill="none" stroke="#00ab8e" stroke-width="1.3" stroke-linecap="round" stroke-linejoin="round"/>
    </symbol>
  </defs>
</svg>

<!-- ============ OUTSIDE SHEET ============ -->
<section class="sheet sheet--outside">
  <svg class="sheet-bg" width="670" height="521" aria-hidden="true">
    <defs>
      <linearGradient id="g-photo-fade" x1="0" y1="0" x2="1" y2="1">
        <stop offset="0" stop-color="#e6edf1"/><stop offset="1" stop-color="#4d5a64"/>
      </linearGradient>
    </defs>
    <rect width="670" height="521" fill="#fff"/>
    <path d="M0 0H222V20Q110 24 0 58Z" fill="url(#g-grey)"/>
    <path d="M0 410Q110 448 222 472V521H0Z" fill="url(#g-grey-v)"/>
    <rect x="222" y="0" width="220" height="478" fill="url(#g-teal-panel)"/>
    <path d="M442 0H670V40Q560 14 442 30Z" fill="url(#g-grey)"/>
    <path d="M442 472Q560 462 670 418V428Q560 468 442 480Z" fill="#00ab8e"/>
    <path d="M442 480Q560 468 670 428V521H442Z" fill="url(#g-grey-v)"/>
    <rect x="0" y="478" width="670" height="10" fill="#cfcfcf"/>
    <rect x="0" y="488" width="670" height="17" fill="#f7f7f7"/>
    <rect x="0" y="505" width="670" height="16" fill="#bdbdbd"/>
    <path d="M508 140A135 135 0 0 1 720 80" fill="none" stroke="#c6efe9" stroke-width="5"/>
    <circle cx="616" cy="207" r="132" fill="none" stroke="#00ab8e" stroke-width="5" stroke-dasharray="300 600" transform="rotate(-150 616 207)"/>
    <circle cx="616" cy="207" r="126" fill="#8f9ba5" role="img" aria-label="Photo of a laptop showing accounting dashboards on a desk">
      <title>Photo of a laptop showing accounting dashboards on a desk</title>
    </circle>
    <circle cx="616" cy="207" r="126" fill="url(#g-photo-fade)" opacity=".6"/>
    <path d="M540 430H660" stroke="#00ab8e" stroke-width="1"/>
  </svg>

  <!-- Services panel -->
  <div class="tab tab--teal" style="left:0;top:31px;min-width:111px;height:29px;padding-left:15px;font-size:11px">Services Available</div>

  <svg class="svc" style="left:42.5px;top:83.5px" viewBox="0 0 57 57" aria-hidden="true"><use href="#svc-ring"/>
    <g fill="none" stroke="#fff" stroke-width="1.5" stroke-linejoin="round"><rect x="22" y="16" width="16" height="11" transform="rotate(30 30 21)"/><path d="M16 36h8l6 3 9-5"/><path d="M16 33h6"/></g></svg>
  <div class="svc-label" style="left:29px;top:145px">Reconcile &amp; Pay<br>Agency Bill<br>Premiums</div>

  <svg class="svc" style="left:121.5px;top:83.5px" viewBox="0 0 57 57" aria-hidden="true"><use href="#svc-ring"/>
    <g fill="none" stroke="#fff" stroke-width="1.5"><circle cx="28.5" cy="17" r="4"/></g>
    <ellipse cx="29" cy="32" rx="11" ry="7.5" fill="#fff"/><rect x="22" y="36" width="3" height="5" fill="#fff"/><rect x="32" y="36" width="3" height="5" fill="#fff"/></svg>
  <div class="svc-label" style="left:108px;top:145px">Record<br>Direct Bill<br>Commission</div>

  <svg class="svc" style="left:42.5px;top:175.5px" viewBox="0 0 57 57" aria-hidden="true"><use href="#svc-ring"/>
    <g fill="none" stroke="#fff" stroke-width="1.5"><path d="M20 14h12l5 5v23H20Z"/><path d="M24 22h9M24 26h9M28 32h6M28 36h6"/></g>
    <text x="21" y="39" fill="#fff" font-size="10" font-weight="700" font-family="Montserrat,sans-serif">$</text></svg>
  <div class="svc-label" style="left:29px;top:237px">Prepare &amp;<br>Interpret<br>Financial<br>Statement</div>

  <svg class="svc" style="left:121.5px;top:175.5px" viewBox="0 0 57 57" aria-hidden="true"><use href="#svc-ring"/>
    <g fill="none" stroke="#fff" stroke-width="1.4"><rect x="17" y="14" width="20" height="27"/><path d="M21 22v-4M25 22v-5M29 22v-3M33 22v-5M20 26h14M20 30h14M20 34h10"/><rect x="32" y="31" width="9" height="11" fill="url(#g-circle)"/></g></svg>
  <div class="svc-label" style="left:108px;top:237px">Reconcile<br>General Ledger<br>Accounts</div>

  <svg class="svc" style="left:42.5px;top:273.5px" viewBox="0 0 57 57" aria-hidden="true"><use href="#svc-ring"/>
    <g fill="none" stroke="#fff" stroke-width="1.4"><path d="M16 16h25v22l-3 2-3-2-3 2-3-2-3 2-3-2-3 2-3-2Z"/><path d="M28 22h10M28 26h10M28 30h10"/></g>
    <text x="18" y="33" fill="#fff" font-size="12" font-weight="700" font-family="Montserrat,sans-serif">$</text></svg>
  <div class="svc-label" style="left:29px;top:335px">Reconcile<br>Customer<br>Accounts<br>Receivable</div>

  <svg class="svc" style="left:121.5px;top:273.5px" viewBox="0 0 57 57" aria-hidden="true"><use href="#svc-ring"/>
    <g fill="none" stroke="#fff" stroke-width="1.4"><path d="M18 13h21v24l-6 6H18Z"/><path d="M21 22h15M21 26h15M21 30h10"/><circle cx="23" cy="37" r="2"/></g>
    <rect x="19" y="15" width="19" height="4" fill="#fff"/></svg>
  <div class="svc-label" style="left:108px;top:335px">Pay Vendor<br>Invoices</div>

  <svg class="svc" style="left:85.5px;top:362.5px" viewBox="0 0 57 57" aria-hidden="true"><use href="#svc-ring"/>
    <g fill="none" stroke="#fff" stroke-width="1.6"><rect x="17" y="23" width="22" height="17" rx="3"/><path d="M31 29h9v6h-9Z"/><path d="M21 23l6-7 5 5"/></g>
    <text x="24" y="22" fill="#fff" font-size="7" font-weight="700" font-family="Montserrat,sans-serif">$</text></svg>
  <div class="svc-label" style="left:72px;top:424px">Process Payroll</div>

  <!-- How it works panel -->
  <div class="tab tab--white" style="left:222px;top:32px;min-width:163px;height:27px;padding-left:17px;font-size:10px">How Outsourcing to MTLS Works</div>
  <p class="body-text" style="left:239px;top:71px;width:186px;color:#fff">We access your Velmont Orbis online database in the same manner as Agency staff. You provide the login credentials. Below is a high-level overview of the process. A detailed operational workflow is provided to each client Agency.</p>

  <div class="steps">
    <div class="step-line" style="top:140px;height:260px;left:-3.5px"></div>
    <div class="step" style="top:126px"><svg class="step-tick" width="9" height="9"><use href="#tick"/></svg>Agency staff routes accounting documents to MTLS through Velmont Orbis.</div>
    <div class="step" style="top:153px"><svg class="step-tick" width="9" height="9"><use href="#tick"/></svg>Agency staff makes bank deposits of paper checks and cash, routing documentation to MTLS to record in Velmont Orbis. MTLS records EFT transactions from the bank records.</div>
    <div class="step" style="top:197px"><svg class="step-tick" width="9" height="9"><use href="#tick"/></svg>MTLS pays your vendors and insurance companies/brokers via Velmont Orbis checks that you print, or via your bank's bill pay system, or via ACH. Agencies may choose the method.</div>
    <div class="step" style="top:251px"><svg class="step-tick" width="9" height="9"><use href="#tick"/></svg>MTLS reconciles Agency staff invoicing on all agency bill transactions with insurance company/broker records at time of payment. We work with your staff on discrepancies.</div>
    <div class="step" style="top:296px"><svg class="step-tick" width="9" height="9"><use href="#tick"/></svg>MTLS records all direct bill commission at the time commission is received; this includes downloads, imports, and manual entry. You provide the commission statements or provide online access for MTLS to obtain.</div>
    <div class="step" style="top:358px"><svg class="step-tick" width="9" height="9"><use href="#tick"/></svg>MTLS reconciles all bank accounts in Velmont Orbis with your bank's data at least twice per week. You provide the login credentials.</div>
    <div class="step" style="top:394px"><svg class="step-tick" width="9" height="9"><use href="#tick"/></svg>MTLS sends financial statements to Agency Principals each month. We encourage review and discussion.</div>
  </div>

  <svg class="abs" style="left:252px;top:431px" width="32" height="32" aria-hidden="true">
    <circle cx="16" cy="16" r="14.5" fill="none" stroke="#fff" stroke-width="1.6"/>
    <path d="M11 9c-1.5 1-2 3 0 7s5 6.5 7 7 3-.5 4-2l-3-2.5-1.6 1.3c-1.5-.6-3.5-2.6-4-4l1.3-1.6L12 9Z" fill="#fff"/>
  </svg>
  <div class="abs" style="left:291px;top:436px;font-size:17.5px;font-weight:500;color:#fff;letter-spacing:.3px">555.014.2290</div>
  <div class="abs" style="left:301px;top:472px;width:61px;height:1px;background:#fff;opacity:.8"></div>

  <!-- Cover panel -->
  <div class="brand"><span class="brand-mark"></span><span class="brand-name">MTLS</span></div>
  <div class="brand-full">Marrowfield Tally &amp; Ledger Services</div>

  <svg class="abs" style="left:474px;top:111px" width="48" height="48" aria-hidden="true">
    <circle cx="24" cy="24" r="23" fill="#fff" stroke="#bdbdbd" stroke-width="2"/>
    <g fill="none" stroke="#00ab8e" stroke-width="1.6"><ellipse cx="22" cy="16" rx="8" ry="3"/><path d="M14 16v14c0 1.7 3.6 3 8 3M30 16v7M14 21c0 1.7 3.6 3 8 3s8-1.3 8-3M14 26c0 1.7 3.6 3 8 3"/></g>
    <circle cx="31" cy="30" r="5" fill="#00ab8e"/><path d="M28.8 30l1.6 1.6 2.8-3" fill="none" stroke="#fff" stroke-width="1.2"/>
  </svg>
  <div class="feature-label" style="left:449px;top:164px">DATA SECURITY</div>

  <svg class="abs" style="left:452px;top:179px" width="56" height="56" aria-hidden="true">
    <circle cx="28" cy="28" r="27" fill="#fff" stroke="#bdbdbd" stroke-width="2"/>
    <circle cx="28" cy="28" r="12" fill="#00ab8e" stroke="#00ab8e" stroke-width="4" stroke-dasharray="3 2"/>
    <circle cx="28" cy="28" r="7" fill="#fff"/><path d="M24.5 28l2.5 2.5 4.5-5" fill="none" stroke="#00ab8e" stroke-width="1.8"/>
  </svg>
  <div class="feature-label" style="left:449px;top:242px">QUALITY CONTROL</div>

  <svg class="abs" style="left:486px;top:251px" width="66" height="66" aria-hidden="true">
    <circle cx="33" cy="33" r="32" fill="#fff" stroke="#bdbdbd" stroke-width="2"/>
    <circle cx="33" cy="33" r="8" fill="none" stroke="#00ab8e" stroke-width="3" stroke-dasharray="3 1.5"/>
    <circle cx="33" cy="33" r="3.5" fill="none" stroke="#00ab8e" stroke-width="1.4"/>
    <path d="M19 30a14 14 0 0 1 24-8M47 36a14 14 0 0 1-24 8" fill="none" stroke="#00ab8e" stroke-width="1.8"/>
    <path d="M43 17v6h-6M23 49v-6h6" fill="none" stroke="#00ab8e" stroke-width="1.8"/>
  </svg>
  <div class="feature-label" style="left:466px;top:330px">SEPARATION OF DUTIES</div>

  <svg class="abs" style="left:572px;top:270px" width="72" height="72" aria-hidden="true">
    <circle cx="36" cy="36" r="35" fill="#fff" stroke="#bdbdbd" stroke-width="2"/>
    <g fill="#00ab8e"><circle cx="36" cy="31" r="4.5"/><path d="M27 46c0-6 4-9 9-9s9 3 9 9Z"/><circle cx="24" cy="34" r="3.5"/><path d="M17 46c0-5 3-7 7-7 2 0 3 .5 4 1-1.5 1.5-2 3.5-2 6Z"/><circle cx="48" cy="34" r="3.5"/><path d="M55 46c0-5-3-7-7-7-2 0-3 .5-4 1 1.5 1.5 2 3.5 2 6Z"/></g>
  </svg>
  <div class="feature-label" style="left:537px;top:350px">EDUCATED &amp; TRAINED STAFF</div>

  <h1 class="headline">NEED HELP WITH<br><span class="alt">VELMONT ORBIS</span><br><strong>ACCOUNTING?</strong></h1>

  <div class="web" style="left:0;color:var(--ink)">WWW.MARROWFIELDLEDGER.COM</div>
  <div class="web" style="left:223px;color:var(--teal)">WWW.MARROWFIELDLEDGER.COM</div>
  <div class="web" style="left:446px;color:var(--ink)">WWW.MARROWFIELDLEDGER.COM</div>
</section>

<!-- ============ INSIDE SHEET ============ -->
<section class="sheet sheet--inside">
  <svg class="sheet-bg" width="670" height="521" aria-hidden="true">
    <defs>
      <linearGradient id="g-warm" x1="0" y1="0" x2="1" y2="1">
        <stop offset="0" stop-color="#d8c8b0"/><stop offset=".6" stop-color="#8d7f72"/><stop offset="1" stop-color="#3a3a3c"/>
      </linearGradient>
      <linearGradient id="g-desk" x1="0" y1="0" x2="1" y2="1">
        <stop offset="0" stop-color="#f2f2f2"/><stop offset="1" stop-color="#b9b9b9"/>
      </linearGradient>
    </defs>
    <rect width="447" height="521" fill="#fff"/>
    <rect width="447" height="160" fill="url(#g-grey)"/>
    <path d="M0 0H222V521H0Z" fill="url(#g-grey-v)"/>
    <path d="M0 208Q110 168 222 150V521H0Z" fill="url(#g-teal-panel)"/>
    <path d="M222 150Q330 140 447 130V521H222Z" fill="#fff"/>
    <rect x="394" y="0" width="53" height="134" fill="url(#g-desk)" role="img" aria-label="Photo of business stationery on a desk"><title>Photo of business stationery on a desk</title></rect>
    <rect x="447" width="223" height="521" fill="url(#g-teal-panel)"/>
    <path d="M447 521V480Q520 405 670 388V521Z" fill="#0a6e62"/>
    <path d="M452 521V486Q525 414 670 398V521Z" fill="url(#g-warm)" role="img" aria-label="Photo of hands using a tablet with charts"><title>Photo of hands using a tablet with charts</title></path>
    <rect x="0" y="500" width="447" height="13" fill="#f7f7f7"/>
    <rect x="0" y="513" width="222" height="8" fill="#00ab8e"/>
    <rect x="222" y="513" width="225" height="8" fill="#e6e6e6"/>
    <path d="M626 427H224V494H426Q443 494 443 478V440Q443 427 426 427Z" fill="#f3f3f3"/>
    <path d="M242 465H421" stroke="#00ab8e" stroke-width=".8"/>

    <g>
      <path d="M143 26A55 55 0 1 0 143 124" fill="none" stroke="#e0e0e0" stroke-width="6"/>
      <circle cx="112" cy="75" r="47" fill="#8a8f94" role="img" aria-label="Portrait of Owen Harrick"><title>Portrait of Owen Harrick</title></circle>
      <path d="M143 188A55 55 0 1 0 143 286" fill="none" stroke="#e0e0e0" stroke-width="6"/>
      <circle cx="112" cy="237" r="47" fill="#9a9890" role="img" aria-label="Portrait of Lena Marsh"><title>Portrait of Lena Marsh</title></circle>
      <path d="M143 327A55 55 0 1 0 143 425" fill="none" stroke="#e0e0e0" stroke-width="6"/>
      <circle cx="112" cy="376" r="47" fill="#8d9096" role="img" aria-label="Portrait of Tobin Vareck"><title>Portrait of Tobin Vareck</title></circle>
      <path d="M364 157A55 55 0 1 0 364 255" fill="none" stroke="#67d7c9" stroke-width="6"/>
      <circle cx="333" cy="206" r="49" fill="#9b928a" role="img" aria-label="Portrait of Ruth Calloway"><title>Portrait of Ruth Calloway</title></circle>
    </g>
  </svg>

  <!-- Team panel -->
  <div class="person-name" style="left:0;top:134px">Owen Harrick</div>
  <div class="person-role" style="left:0;top:145px;color:var(--teal)">Director of Accounting</div>
  <div class="person-name" style="left:0;top:296px;color:#fff">Lena Marsh</div>
  <div class="person-role" style="left:0;top:307px;color:var(--ink)">Accountant</div>
  <div class="person-name" style="left:0;top:438px;color:#fff">Tobin Vareck</div>
  <div class="person-role" style="left:0;top:449px;color:var(--ink)">Accountant</div>
  <div class="abs" style="left:19px;top:471px;font-family:'Oswald',sans-serif;font-weight:500;font-size:8.8px;line-height:10px;color:#fff">FOR A COMPLETE LIST OF MTLS STAFF AND THEIR PROFILES,<br>PLEASE VISIT WWW.MARROWFIELDLEDGER.COM</div>
  <div class="web" style="left:0;top:502px;color:var(--ink);width:222px">WWW.MARROWFIELDLEDGER.COM</div>

  <!-- Contact + founder panel -->
  <h2 class="contact-line" style="top:10px;font-size:15.5px;font-weight:500">GET IN <span style="color:var(--teal);font-weight:600">TOUCH</span></h2>
  <svg class="abs" style="left:360px;top:30px" width="18" height="18" aria-hidden="true"><circle cx="9" cy="9" r="9" fill="#00ab8e"/><path d="M9 4a3.3 3.3 0 0 0-3.3 3.3C5.7 10 9 14 9 14s3.3-4 3.3-6.7A3.3 3.3 0 0 0 9 4Z" fill="none" stroke="#fff" stroke-width="1.1"/><circle cx="9" cy="7.4" r="1.1" fill="#fff"/></svg>
  <div class="contact-line" style="top:50px;font-size:8.8px;line-height:11.5px;font-weight:500;letter-spacing:.6px">47 ALDER MILL ROAD<br>KESTREL FALLS, CT 06000</div>
  <svg class="abs" style="left:360px;top:74px" width="18" height="18" aria-hidden="true"><circle cx="9" cy="9" r="9" fill="#00ab8e"/><path d="M6.3 5c-.9.6-1.2 1.8 0 4.2s3 3.9 4.2 4.2 1.8-.3 2.4-1.2l-1.8-1.5-1 .8c-.9-.4-2-1.6-2.4-2.4l.8-1L7.2 5Z" fill="#fff"/></svg>
  <div class="contact-line" style="top:93px;font-size:13px;font-weight:500">555.014.2290</div>
  <svg class="abs" style="left:360px;top:109px" width="18" height="18" aria-hidden="true"><circle cx="9" cy="9" r="9" fill="#00ab8e"/><g fill="none" stroke="#fff" stroke-width=".9"><circle cx="9" cy="9" r="4.6"/><ellipse cx="9" cy="9" rx="2" ry="4.6"/><path d="M4.4 9h9.2"/></g></svg>
  <div class="contact-line" style="top:129px;font-size:7.3px;font-weight:500">WWW.MARROWFIELDLEDGER.COM</div>

  <div class="abs" style="left:222px;top:267px;width:225px;text-align:center;font-size:8.8px;font-weight:500;color:var(--teal)">Ruth Calloway</div>
  <div class="abs" style="left:222px;top:278px;width:225px;text-align:center;font-size:7.6px;font-weight:600">Founder</div>
  <p class="body-text" style="left:235px;top:290px;width:199px;color:var(--ink);text-align-last:center">MTLS's mission is to provide Independent Insurance Agencies a resource to have their accounting and bookkeeping performed accurately, timely and cost effectively. MTLS's 35 member staff is led by Ruth Calloway. Ruth worked in Independent Insurance Agencies for several years before forming MTLS in 2011. Her experience includes accounting, operational management, and client service. She earned a bachelor's degree in accounting from Northbrook State University and a master's degree in business administration from Eastvale University. Ruth is an adjunct accounting professor at Riverside Community Colleges. She serves her community as President of the local Civic Club.</p>

  <div class="abs" style="left:222px;top:430px;width:221px;text-align:center;font-weight:800;color:#555;font-size:18.5px;line-height:18px">LET MTLS BE</div>
  <div class="abs" style="left:222px;top:449px;width:221px;text-align:center;font-weight:700;color:#777;font-size:10px;line-height:11px">AN INTEGRAL PART OF</div>
  <div class="abs" style="left:222px;top:466px;width:221px;text-align:center;font-weight:700;color:var(--teal);font-size:12.5px;line-height:13px">YOUR AGENCY'S</div>
  <div class="abs" style="left:222px;top:477px;width:221px;text-align:center;font-weight:800;color:var(--teal);font-size:20px;line-height:20px">SUCCESS.</div>
  <div class="web" style="left:222px;top:502px;color:var(--teal);width:225px">WWW.MARROWFIELDLEDGER.COM</div>

  <!-- Security + fees panel -->
  <div class="abs" style="left:463px;top:15px;width:187px;height:22px;background:#fff;border-radius:6px;box-shadow:0 1px 3px rgba(0,0,0,.2);color:var(--teal);font-size:7.4px;font-weight:700;line-height:8.6px;text-align:center;padding-top:2.5px">WE IMPLEMENT CONTROLS FOR<br>DATA SECURITY</div>
  <p class="body-text" style="left:463px;top:49px;width:187px;color:#fff">All computer equipment is owned by MTLS. PCs and routers are regularly updated to stay current with technology. All are continuously monitored for system updates and virus/malware by an independent IT firm. Dual authentication is required for remote access to our PCs. Documents are shared within Velmont Orbis or through a secure document sharing platform, Vaultline.</p>

  <div class="tab tab--white" style="left:446px;top:134px;min-width:179px;height:28px;padding-left:20px;font-size:10.5px">How the MTLS Fees Are Structured</div>
  <p class="body-text" style="left:463px;top:170px;width:187px;color:#fff;font-weight:700;font-size:6.8px">Fees are a flat monthly rate based on annual policy commission revenue. The table below lists sample rates for our full-service offerings at different revenue volumes for an Agency with a typical mix of business and complexity. Fees assume compliance with our standard operating workflows.</p>

  <div class="fee-table">
    <div class="fee-head"><div>Annual Commission Revenue</div><div>Monthly Service Fee</div></div>
    <div class="fee-body">
      <div>&lt;$300,000<br>$700,000<br>$1,000,000<br>$1,500,000<br>$2,000,000<br>$2,500,000<br>$3,000,000</div>
      <div>$600<br>$1,400<br>$2,000<br>$2,500<br>$3,000<br>$3,500<br>$4,500</div>
    </div>
  </div>

  <div class="abs" style="left:463px;top:347px;font-size:8.4px;font-weight:500;color:#fff;white-space:nowrap">We can provide services for larger agencies,</div>
  <div class="abs" style="left:463px;top:358px;font-size:11.5px;line-height:15px;font-weight:700;color:#173f3a">typically supplementing<br>in-house staff.</div>
</section>

</body>
</html>
```